Business Card Design for a Lending Business (Hard Money loans)

We need a business card for our Real Estate Lending business. We do hard Money loans for real estate investors. We have an existing logo we like, see attached. I'd like the business card to mostly include the logo colors, but a bright color pop of some sort would be nice to see also. Card should include Logo, Company Name, Company Address, Employee Name, Cell Phone, Main Phone, Email, Website

Industry/Entity Type

Finance / Lending

Contact Information for Business Card

Logo, Company Name, Company Address, Employee Name, Cell Phone, Main Phone, Email, Website

Requirements
Nice to have
• I'd like the business card to mostly include the logo colors, but a bright color pop of some sort would be nice to see also.

```html
<!DOCTYPE html>
<html lang="en">
<head>
<meta charset="utf-8">
<title>Northgate Lending – Business Card</title>
<link href="https://fonts.googleapis.com/css2?family=Roboto:wght@400;500;700&display=swap" rel="stylesheet">
<style>
  :root {
    --navy: #2a377f;
    --cyan: #00aedd;
    --white: #ffffff;
    --paper: #f0f0f0;
    --backdrop: #e6e6e6;
    --ink: #4a4a4a;
  }
  * { margin: 0; padding: 0; box-sizing: border-box; }
  html, body {
    width: 1200px; height: 1200px; overflow: hidden;
    background: var(--backdrop);
    font-family: "Roboto", Arial, sans-serif;
  }
  .canvas { position: relative; width: 1200px; height: 1200px; }
  .card {
    position: absolute; left: 214px; width: 779px; height: 468px; overflow: hidden;
  }
  .card--front { top: 88px; background: var(--navy); }
  .card--back { top: 648px; background: var(--paper); border: 1px solid var(--navy); }
  .stripes { position: absolute; inset: 0; width: 100%; height: 100%; }

  .brand { position: absolute; text-align: center; font-weight: 700; }
  .brand__dot { display: block; margin: 0 auto 18px; border-radius: 50%; }
  .brand__name { display: block; letter-spacing: 6px; line-height: 1; }
  .brand__sub { display: block; letter-spacing: 9px; line-height: 1; margin-top: 10px; }

  .card--front .brand { left: 0; right: 0; top: 150px; color: var(--white); }
  .card--front .brand__dot { width: 74px; height: 74px; background: var(--white); }
  .card--front .brand__name { font-size: 40px; }
  .card--front .brand__sub { font-size: 17px; }

  .card--back .brand { left: 424px; width: 270px; top: 136px; color: var(--navy); }
  .card--back .brand__dot { width: 64px; height: 64px; background: var(--navy); }
  .card--back .brand__name { font-size: 33px; letter-spacing: 5px; }
  .card--back .brand__sub { font-size: 15px; letter-spacing: 8px; }

  .person { position: absolute; left: 52px; top: 50px; }
  .person__name { font-size: 34px; font-weight: 500; color: var(--navy); line-height: 1.1; letter-spacing: -0.3px; }
  .person__role { font-size: 19px; color: var(--ink); line-height: 1.1; margin-top: 2px; }

  .contacts { position: absolute; left: 52px; top: 187px; list-style: none; }
  .contacts__item { display: flex; align-items: center; margin-bottom: 18px; }
  .contacts__icon { width: 26px; height: 26px; flex: none; margin-right: 19px; color: var(--navy); }
  .contacts__text { font-size: 17px; font-weight: 500; color: var(--ink); line-height: 21px; }

  .divider {
    position: absolute; left: 388px; top: 129px; width: 2px; height: 211px;
    background: var(--navy);
  }
</style>
</head>
<body>
<main class="canvas">

  <section class="card card--front" aria-label="Card front">
    <svg class="stripes" viewBox="0 0 1246 748" preserveAspectRatio="none" aria-hidden="true">
      <g fill="var(--white)">
        <polygon points="0,0 27,0 0,27"/>
        <polygon points="87,0 162,0 0,162 0,87"/>
        <polygon points="227,0 297,0 0,297 0,227"/>
        <polygon points="362,0 434,0 0,434 0,362"/>
      </g>
      <g fill="var(--cyan)">
        <polygon points="52,450 88,487 0,574 0,499"/>
        <polygon points="120,518 156,556 0,709 0,639"/>
        <polygon points="188,586 225,624 102,748 29,748"/>
        <polygon points="257,654 295,691 239,748 165,748"/>
      </g>
    </svg>
    <div class="brand">
      <span class="brand__dot"></span>
      <span class="brand__name">NORTHGATE</span>
      <span class="brand__sub">LENDING</span>
    </div>
  </section>

  <section class="card card--back" aria-label="Card back">
    <svg class="stripes" viewBox="0 0 1246 748" preserveAspectRatio="none" aria-hidden="true">
      <g fill="var(--navy)">
        <polygon points="812,0 882,0 1246,364 1246,434"/>
        <polygon points="947,0 1017,0 1246,229 1246,299"/>
        <polygon points="1082,0 1157,0 1246,89 1246,164"/>
        <polygon points="1219,0 1246,0 1246,27"/>
      </g>
      <g fill="var(--cyan)">
        <polygon points="1157,486 1194,451 1246,499 1246,572"/>
        <polygon points="1089,554 1125,518 1246,636 1246,709"/>
        <polygon points="1020,621 1057,586 1215,748 1142,748"/>
        <polygon points="950,689 987,654 1079,748 1007,748"/>
      </g>
    </svg>

    <div class="person">
      <h1 class="person__name">DANIEL REYES</h1>
      <p class="person__role">GRAPHIC DESIGNER</p>
    </div>

    <ul class="contacts">
      <li class="contacts__item">
        <svg class="contacts__icon" viewBox="0 0 24 24" aria-hidden="true"><path fill="currentColor" d="M6.6 2.5l2.6 4.2-1.8 1.6c.9 2.6 2.9 5.6 5.4 7.6l1.9-1.4 3.8 2.9-1.5 2.6c-5.4-.9-11-7.5-11.4-14.6z"/></svg>
        <span class="contacts__text">+001234 56 789<br>+001234 56 789</span>
      </li>
      <li class="contacts__item">
        <svg class="contacts__icon" viewBox="0 0 24 24" aria-hidden="true"><rect x="1.5" y="6" width="21" height="13" fill="none" stroke="currentColor" stroke-width="1.4"/><path d="M1.5 6l10.5 8 10.5-8M1.5 19l8-6.5M22.5 19l-8-6.5" fill="none" stroke="currentColor" stroke-width="1.2"/></svg>
        <span class="contacts__text">company site here<br>website name here</span>
      </li>
      <li class="contacts__item">
        <svg class="contacts__icon" viewBox="0 0 24 24" aria-hidden="true"><path fill="currentColor" d="M12 1.5a5.5 5.5 0 0 0-5.5 5.5c0 4 5.5 10 5.5 10s5.5-6 5.5-10A5.5 5.5 0 0 0 12 1.5zm0 7.7a2.2 2.2 0 1 1 0-4.4 2.2 2.2 0 0 1 0 4.4z"/><ellipse cx="12" cy="19.5" rx="10" ry="3" fill="none" stroke="currentColor" stroke-width="1.6"/></svg>
        <span class="contacts__text">address name here<br>city name here - 1234</span>
      </li>
      <li class="contacts__item">
        <svg class="contacts__icon" viewBox="0 0 24 24" aria-hidden="true"><circle cx="12" cy="12" r="10" fill="currentColor"/><path d="M2 12h20M12 2c-3.5 3-3.5 17 0 20M12 2c3.5 3 3.5 17 0 20M4 7h16M4 17h16" fill="none" stroke="var(--paper)" stroke-width="1"/></svg>
        <span class="contacts__text">www.yourwebsite.com</span>
      </li>
    </ul>

    <div class="divider" aria-hidden="true"></div>

    <div class="brand">
      <span class="brand__dot"></span>
      <span class="brand__name">NORTHGATE</span>
      <span class="brand__sub">LENDING</span>
    </div>
  </section>

</main>
</body>
</html>
```